Brookhurst Dental Care
Daniel K. Pruitt DMD
Professional
5283 E. Copper Ridge Ave, Suite B-4
Phoenix, AZ 85019
office@brookhurstdental.com
www.brookhurstdental.com
Please incorporate my name:
under the Brookhurst Dental Care logo
Use standard format to write in scheduled appointments.
Also include at bottom:
"We appreciate a 24 hr. notice for cancellations"

```html
<!DOCTYPE html>
<html lang="en">
<head>
<meta charset="utf-8">
<title>Brookhurst Dental Care — Stationery</title>
<link href="https://fonts.googleapis.com/css2?family=Lato:wght@400;700&display=swap" rel="stylesheet">
<style>
  :root{
    --bg:#ffffff;
    --paper:#ffffff;
    --edge:#d9d9d9;
    --brand:#2f6b2a;
    --accent-a:#e0481d;
    --accent-b:#f6a81c;
    --accent-line:#6a9a2f;
    --ink:#555555;
    --rule:#b5b5b5;
    --floor:#e6e6e6;
  }
  *{box-sizing:border-box;margin:0;padding:0}
  html,body{width:1200px;height:482px;overflow:hidden;background:var(--bg)}
  body{position:relative;font-family:"Lato",Arial,sans-serif;color:var(--ink)}

  .piece{position:absolute;background:var(--paper);border:1px solid var(--edge);box-shadow:0 1px 3px rgba(0,0,0,.12);overflow:hidden}
  .stripe{position:absolute;left:0;right:0;top:0;height:6px;background:linear-gradient(90deg,var(--accent-a),var(--accent-b));border-bottom:2px solid var(--accent-line)}

  .brand{display:flex;align-items:center;gap:5px;color:var(--brand);font-weight:700;text-transform:uppercase;letter-spacing:.4px;white-space:nowrap}
  .brand-dot{width:9px;height:9px;border-radius:50%;background:var(--brand);flex:none}

  .contact{font-size:6.2px;line-height:8.4px;color:var(--ink)}

  /* letter-size sheets */
  .sheet{top:24px;width:276px;height:408px}
  .sheet--fax{left:19px}
  .sheet--letter{left:780px}
  .sheet .brand{position:absolute;left:14px;top:18px;font-size:13px}
  .sheet .contact{position:absolute;left:14px;top:38px}

  .fax-fields{position:absolute;left:16px;top:138px;width:244px;display:grid;grid-template-columns:1fr 1fr;column-gap:14px;row-gap:12px}
  .field{display:flex;align-items:flex-end;font-size:6.5px;gap:4px}
  .field span{width:20px}
  .field i{flex:1;border-bottom:1px solid var(--rule);height:7px}
  .fax-checks{position:absolute;left:16px;top:258px;display:flex;gap:9px;font-size:5.6px}
  .check{display:flex;align-items:center;gap:2px}
  .check b{width:5px;height:5px;border:1px solid var(--ink);border-radius:50%}

  /* envelopes */
  .envelope{left:396px;width:336px}
  .envelope--front{top:67px;height:144px}
  .envelope--front .brand{position:absolute;left:12px;top:16px;font-size:13px}
  .envelope--front .contact{position:absolute;left:12px;top:36px}
  .envelope--back{top:230px;height:154px}
  .envelope--back svg{position:absolute;inset:0}
  .envelope--back .brand{position:absolute;left:50%;top:58px;transform:translateX(-50%);font-size:8px}

  /* business cards */
  .card{left:931px;width:245px}
  .card--front{top:101px;height:127px}
  .card--front .brand{position:absolute;left:10px;top:16px;font-size:11px}
  .card--front .holder{position:absolute;right:12px;top:50px;font-size:7px;color:var(--ink)}
  .card--front .contact{position:absolute;left:10px;bottom:10px;font-size:5.6px;line-height:7.6px}
  .card--back{top:240px;height:132px}
  .card--back .brand{position:absolute;left:50%;top:14px;transform:translateX(-50%);font-size:8px}
  .appointment{position:absolute;left:22px;right:22px;top:62px;display:flex;align-items:flex-end;gap:5px;font-size:6px}
  .appointment i{flex:1;border-bottom:1px solid var(--rule);height:7px}
  .notice{position:absolute;left:0;right:0;bottom:18px;text-align:center;font-size:5.8px}

  .floor{position:absolute;left:10px;right:10px;top:458px;height:1px;background:var(--floor)}
</style>
</head>
<body>

  <section class="piece sheet sheet--fax">
    <div class="stripe"></div>
    <div class="brand"><span class="brand-dot"></span>Brookhurst Dental Care</div>
    <div class="contact">
      5283 E. Copper Ridge Ave, Suite B-4 • Phoenix, AZ 85019<br>
      Phone (602) 555-0148 • Fax (602) 555-0149<br>
      office@brookhurstdental.com • www.brookhurstdental.com
    </div>
    <div class="fax-fields">
      <div class="field"><span>To:</span><i></i></div>
      <div class="field"><span>From:</span><i></i></div>
      <div class="field"><span>Fax:</span><i></i></div>
      <div class="field"><span>Pages:</span><i></i></div>
      <div class="field"><span>Phone:</span><i></i></div>
      <div class="field"><span>Date:</span><i></i></div>
      <div class="field"><span>Re:</span><i></i></div>
      <div class="field"><span>CC:</span><i></i></div>
    </div>
    <div class="fax-checks">
      <div class="check"><b></b>Urgent</div>
      <div class="check"><b></b>For Review</div>
      <div class="check"><b></b>Please Comment</div>
      <div class="check"><b></b>Please Reply</div>
      <div class="check"><b></b>Please Recycle</div>
    </div>
  </section>

  <section class="piece envelope envelope--front">
    <div class="stripe"></div>
    <div class="brand"><span class="brand-dot"></span>Brookhurst Dental Care</div>
    <div class="contact">
      5283 E. Copper Ridge Ave, Suite B-4 • Phoenix, AZ 85019<br>
      office@brookhurstdental.com • www.brookhurstdental.com
    </div>
  </section>

  <section class="piece envelope envelope--back">
    <svg width="336" height="154" viewBox="0 0 336 154">
      <polyline points="0,2 168,78 336,2" fill="none" stroke="#cfcfcf" stroke-width="1"/>
      <line x1="0" y1="154" x2="150" y2="86" stroke="#e2e2e2" stroke-width="1"/>
      <line x1="336" y1="154" x2="186" y2="86" stroke="#e2e2e2" stroke-width="1"/>
    </svg>
    <div class="brand"><span class="brand-dot"></span>Brookhurst</div>
  </section>

  <section class="piece sheet sheet--letter">
    <div class="stripe"></div>
    <div class="brand"><span class="brand-dot"></span>Brookhurst Dental Care</div>
    <div class="contact">
      5283 E. Copper Ridge Ave, Suite B-4 • Phoenix, AZ 85019<br>
      Phone (602) 555-0148 • Fax (602) 555-0149<br>
      office@brookhurstdental.com • www.brookhurstdental.com
    </div>
  </section>

  <section class="piece card card--front">
    <div class="stripe"></div>
    <div class="brand"><span class="brand-dot"></span>Brookhurst Dental Care</div>
    <div class="holder">Daniel K. Pruitt DMD</div>
    <div class="contact">
      5283 E. Copper Ridge Ave, Suite B-4<br>
      Phoenix, AZ 85019 • Phone (602) 555-0148<br>
      office@brookhurstdental.com<br>
      www.brookhurstdental.com
    </div>
  </section>

  <section class="piece card card--back">
    <div class="brand"><span class="brand-dot"></span>Brookhurst</div>
    <div class="appointment">Your appointment:<i></i></div>
    <div class="notice">We appreciate a 24 hr. notice for cancellations</div>
  </section>

  <div class="floor"></div>

</body>
</html>
```